Elegant wordpress web page for wedding rental of hand sanitizers

We want to rent our hand sanitizing towers out for high-end weddings. We need a very elegant, sophisticated page that describes our offering. You can see an ugly first draft here: trelvo.com/weddings
Target Market(s)
Wedding planners, wedding parents
Number of Pages Required
1 page
Font styles to use
Serif
Script
Colors
Designer to choose colors to be used in the design.
Requirements
Nice to have
- Two wedding-related sites for inspiration: quietorchardweddings-dot-com and fernlaneservices-dot-com

```html
<!DOCTYPE html>
<html lang="en">
<head>
<meta charset="utf-8">
<title>Trelvo — Wedding Sanitizing Stations</title>
<link rel="stylesheet" href="https://fonts.googleapis.com/css2?family=Berkshire+Swash&family=Lora:wght@400;600&display=swap">
<style>
:root{
  --cream:#f8f2e9;
  --sand:#ebe0cc;
  --ink:#2f2a26;
  --white:#ffffff;
  --hero-a:#c9b89c;
  --hero-b:#e8ddca;
  --photo-a:#8e8a72;
  --photo-b:#d9cfc0;
}
*{margin:0;padding:0;box-sizing:border-box}
html,body{width:1200px;height:3242px;overflow:hidden}
body{background:var(--cream);color:var(--ink);font-family:'Lora',serif;position:relative}
.abs{position:absolute}
.script{font-family:'Berkshire Swash',cursive;font-weight:400}

.hero{left:0;top:0;width:1200px;height:562px;background:linear-gradient(160deg,var(--hero-b),var(--hero-a) 55%,#b59c78)}
.nav{left:0;top:0;width:1200px;height:73px;border-bottom:1px solid rgba(255,255,255,.75)}
.logo{left:150px;top:18px;font-family:'Lora',serif;font-weight:600;font-size:24px;color:var(--white)}
.nav-link{top:30px;font-size:12px;color:var(--white);letter-spacing:.3px}
.nav-cta{left:883px;top:26px;width:166px;height:24px;background:var(--white);border-radius:4px;font-size:12px;line-height:24px;text-align:center;color:var(--ink)}
.hero-title{left:0;top:222px;width:1200px;text-align:center;color:var(--white);font-size:44px;line-height:61px}
.hero-arrow{top:300px}

.h2{font-size:25px;left:150px}
.list{left:150px;top:692px;font-size:17.5px;line-height:30px}
.list b{font-weight:600}
.list span{margin-left:12px}
.btn{border:2px solid var(--ink);border-radius:5px;font-size:19px;font-weight:600;text-align:center;background:transparent}
.photo{border-radius:8px;background:linear-gradient(150deg,var(--photo-a),var(--photo-b))}

.card{top:1054px;height:300px;background:var(--sand)}
.card-text{position:absolute;top:178px;font-size:14.5px;line-height:21px}
.card-text b{font-weight:600}
.card-icon{position:absolute;top:120px}

.about-img{left:0;top:1399px;width:599px;height:369px;background:linear-gradient(120deg,#e7ddd0,#cfc3b2)}
.about-panel{left:599px;top:1399px;width:601px;height:369px;background:var(--sand)}
.body-lines{font-size:18px;line-height:30px}

.tile{background:var(--sand);width:390px;height:298px}

.footer{left:0;top:3070px;width:1200px;height:172px;background:var(--sand)}
.foot-text{top:3143px;font-size:17px}
.social{top:3140px;width:28px;height:28px;border-radius:50%;background:var(--ink)}
</style>
</head>
<body>

<div class="abs hero" role="img" aria-label="Wedding reception hall with white chairs, flowers and a photo sanitizing station"></div>
<header class="abs nav">
  <div class="abs logo">Trelvo</div>
  <nav>
    <span class="abs nav-link" style="left:292px">ABOUT</span>
    <span class="abs nav-link" style="left:377px">PRODUCTS</span>
    <span class="abs nav-link" style="left:486px">INDUSTRY SOLUTIONS</span>
    <span class="abs nav-link" style="left:659px">CONTACT</span>
    <span class="abs nav-link" style="left:760px">SEARCH</span>
  </nav>
  <div class="abs nav-cta">MAKE A RESERVATION</div>
</header>
<h1 class="abs hero-title script">Welcome Your Guests With<br>Something Truly Unique<br>- A Customized Hand Sanitizer -</h1>
<svg class="abs hero-arrow" style="left:26px" width="20" height="36" viewBox="0 0 20 36"><path d="M17 2 L3 18 L17 34" fill="none" stroke="#fff" stroke-width="2"/></svg>
<svg class="abs hero-arrow" style="left:1155px" width="20" height="36" viewBox="0 0 20 36"><path d="M3 2 L17 18 L3 34" fill="none" stroke="#fff" stroke-width="2"/></svg>

<section>
  <h2 class="abs h2 script" style="top:645px">What Makes Our Sanitizing Station Better?</h2>
  <div class="abs list">
    <div><b>- Filled with your choice from our wide range of sanitizing solutions -</b></div>
    <div><b>- Easily Customizable -</b><span>choose your preferred backdrop and spout</span></div>
    <div><b>- Durable and Reliable -</b><span>4 ft tall, weighing almost 40 pounds</span></div>
    <div><b>- Touchless and Automatic -</b><span>the preferred way to sanitize</span></div>
    <div><b>- Battery Powered and Wireless -</b><span>locate it anywhere</span></div>
  </div>
  <div class="abs btn" style="left:150px;top:858px;width:284px;height:39px;line-height:35px">Check price and availability</div>
  <div class="abs photo" style="left:790px;top:610px;width:325px;height:325px" role="img" aria-label="Sanitizing station with a couple's photo backdrop on an outdoor wedding aisle"></div>
</section>

<section>
  <h2 class="abs script" style="left:0;width:1192px;text-align:center;top:978px;font-size:25px">Personalize Your Sanitizing Station</h2>
  <div class="abs card" style="left:0;width:292px">
    <svg class="card-icon" style="left:28px" width="38" height="36" viewBox="0 0 38 36" fill="none" stroke="#2f2a26" stroke-width="2"><rect x="8" y="2" width="26" height="24" rx="2"/><rect x="3" y="8" width="26" height="24" rx="2" fill="#ebe0cc"/><circle cx="16" cy="17" r="4"/><path d="M8 28 L16 22 L24 28"/></svg>
    <div class="card-text" style="left:28px"><b>Choose a photo</b><br>The happy couple, the proud parents,<br>even the family dog<br>Use any picture you wish as the<br>backdrop.</div>
  </div>
  <div class="abs card" style="left:302px;width:292px">
    <svg class="card-icon" style="left:29px" width="38" height="36" viewBox="0 0 38 36" fill="none" stroke="#2f2a26" stroke-width="2.5"><path d="M3 32 L18 4 L35 32 Z"/><path d="M10 32 L22 12"/><path d="M17 32 L26 18"/></svg>
    <div class="card-text" style="left:29px"><b>Pick a size and shape</b><br>Any size banner up to 24 x 36 in.<br>Any shape.<br>Send us the photo and we'll print and<br>install it.</div>
  </div>
  <div class="abs card" style="left:605px;width:292px">
    <svg class="card-icon" style="left:32px" width="38" height="36" viewBox="0 0 38 36" fill="none" stroke="#2f2a26" stroke-width="2"><rect x="2" y="2" width="34" height="32" rx="2"/><path d="M12 8 L12 16 Q19 22 26 16 L26 8 L19 13 Z"/><path d="M19 19 L19 26 M8 26 L30 26 L30 30 L8 30 Z"/></svg>
    <div class="card-text" style="left:32px"><b>Decorate the spout</b><br>Use one of our standard decorations<br>- a wedding cake or a flower vase -<br>or specify your own.</div>
  </div>
  <div class="abs card" style="left:907px;width:293px">
    <svg class="card-icon" style="left:69px" width="40" height="38" viewBox="0 0 40 38" fill="none" stroke="#2f2a26" stroke-width="2"><rect x="3" y="10" width="26" height="8"/><rect x="5" y="18" width="22" height="17"/><path d="M16 10 L16 35 M16 10 Q8 0 10 8 M16 10 Q24 0 22 8"/><circle cx="30" cy="28" r="8" fill="#ebe0cc"/><path d="M26 28 L29 31 L34 25"/></svg>
    <div class="card-text" style="left:69px"><b>Our team decorates and<br>delivers the sanitizer</b></div>
  </div>
</section>

<section>
  <div class="abs about-img" role="img" aria-label="Reception hall with a white floral arch and a photo sanitizing station"></div>
  <div class="abs about-panel"></div>
  <h2 class="abs script" style="left:645px;top:1503px;font-size:25px">About Us</h2>
  <div class="abs body-lines" style="left:645px;top:1542px;font-size:17.5px">The most mature, sophisticated and reliable<br>commercial hand sanitizer dispenser<br>on the market today<br>The result of five years of intensive research</div>
</section>

<section>
  <h2 class="abs h2 script" style="top:1862px">Greet your guests with an act of care</h2>
  <div class="abs body-lines" style="left:150px;top:1906px;font-size:17.5px">Make your friends and family feel welcome and safe with a rugged, durable<br>hand sanitizer from Trelvo<br>Our battery-powered dispensers are reliable, wireless, and touchless<br>Filled with your choice from our wide range of sanitizing products</div>
  <div class="abs btn" style="left:150px;top:2044px;width:284px;height:39px;line-height:35px">Check price and availability</div>
  <div class="abs photo" style="left:790px;top:1813px;width:325px;height:324px;background:linear-gradient(150deg,#6e5446,#c9b6a2)" role="img" aria-label="Sanitizing station with a couple's photo in a rustic wooden venue"></div>
</section>

<section>
  <h2 class="abs script" style="left:0;width:1200px;text-align:center;top:2175px;font-size:40px">Portfolio</h2>
  <div class="abs tile" style="left:0;top:2266px"></div>
  <div class="abs tile" style="left:405px;top:2266px"></div>
  <div class="abs tile" style="left:810px;top:2266px"></div>
  <div class="abs tile" style="left:0;top:2580px"></div>
  <div class="abs tile" style="left:405px;top:2580px"></div>
  <div class="abs tile" style="left:810px;top:2580px"></div>
</section>

<section>
  <h2 class="abs script" style="left:0;width:1200px;text-align:center;top:2915px;font-size:39px">Ready to make a reservation?</h2>
  <div class="abs btn" style="left:467px;top:2985px;width:283px;height:39px;line-height:35px">Check price and availability</div>
</section>

<footer class="abs footer"></footer>
<span class="abs foot-text" style="left:150px">© 2021 Trelvo, LLC</span>
<span class="abs foot-text" style="left:457px">Site Map</span>
<span class="abs foot-text" style="left:668px">Privacy Policy</span>
<span class="abs social" style="left:942px"></span>
<span class="abs social" style="left:982px"></span>
<span class="abs social" style="left:1022px"></span>

</body>
</html>
```